Garden Design Flier

I would like a PDF of this half page A4 flier in soft green tones with dark green leaves.

Target Market(s)

Home owners and real estate agents

Font styles to use
Serif
Other font styles liked:
• Papyrus

Colors
acd136
9bcb3c
cadf82
fefdec

Requirements
Must have
• Green tones
Nice to have
• Leaves, vines, lawns
Should not have
• Open to ideas, but classic style

```html
<!DOCTYPE html>
<html lang="en">
<head>
<meta charset="utf-8">
<title>Verdant Gardens – Garden Design Flier</title>
<link rel="stylesheet" href="https://fonts.googleapis.com/css2?family=Didact+Gothic&family=PT+Sans:wght@700&display=swap">
<style>
  :root {
    --page-bg: #ffffff;
    --card-green: #e5efcf;
    --leaf-mid: #9cc47a;
    --leaf-soft: #c7dcae;
    --panel-cream: #f8eee6;
    --frame-gold: #c49a7a;
    --ink-green: #1e4a23;
    --ink-grey: #3a3536;
    --ink-body: #2b2b2b;
  }
  * { margin: 0; padding: 0; box-sizing: border-box; }
  html, body { width: 1200px; height: 928px; overflow: hidden; background: var(--page-bg); }
  .flier {
    position: absolute; left: 30px; top: 61px;
    width: 1140px; height: 806px;
    background: var(--card-green);
    overflow: hidden;
  }
  .foliage { position: absolute; }
  .foliage--top-left {
    left: 0; top: 40px; width: 360px; height: 300px;
    background: radial-gradient(ellipse at 40% 45%, rgba(200,214,170,.9), rgba(229,239,207,0) 70%);
  }
  .foliage--right-vine {
    left: 800px; top: 0; width: 340px; height: 640px;
    background: radial-gradient(ellipse at 60% 40%, var(--leaf-mid), rgba(156,196,122,.4) 45%, rgba(229,239,207,0) 72%);
  }
  .foliage--bottom-left {
    left: 0; top: 320px; width: 260px; height: 486px;
    background: radial-gradient(ellipse at 45% 60%, var(--leaf-mid), rgba(156,196,122,.35) 50%, rgba(229,239,207,0) 75%);
  }
  .foliage--bottom-right {
    left: 960px; top: 560px; width: 220px; height: 246px;
    background: radial-gradient(ellipse at 40% 50%, var(--leaf-soft), rgba(229,239,207,0) 70%);
  }
  .veil {
    position: absolute; left: 129px; top: 66px; width: 878px; height: 672px;
    background: rgba(255,255,255,.22);
  }
  .panel {
    position: absolute; left: 209px; top: 101px; width: 717px; height: 605px;
    background: var(--panel-cream);
  }
  .frame { position: absolute; left: 0; top: 0; width: 1140px; height: 806px; pointer-events: none; }
  .content { position: absolute; left: 251px; top: 0; width: 635px; text-align: center; }
  .brand-name {
    position: absolute; left: 0; width: 100%; top: 200px;
    font-family: 'PT Sans', sans-serif; font-weight: 700; font-size: 60px; line-height: 1;
    color: var(--ink-green);
  }
  .byline, .credential {
    position: absolute; left: 0; width: 100%;
    font-family: 'Didact Gothic', sans-serif; font-size: 21px; line-height: 1;
    color: var(--ink-grey); letter-spacing: 0.02em;
  }
  .byline { top: 319px; }
  .credential { top: 348px; }
  .slogan {
    position: absolute; left: -4px; width: 643px; top: 400px;
    font-family: 'PT Sans', sans-serif; font-weight: 700; font-size: 38.5px; line-height: 1;
    color: var(--ink-green); white-space: nowrap;
  }
  .intro {
    position: absolute; left: 0; width: 100%; top: 459px;
    font-family: 'Didact Gothic', sans-serif; font-size: 19px; line-height: 22px;
    letter-spacing: 0.045em;
    color: var(--ink-body); text-align: justify; text-align-last: left;
  }
  .intro p + p { margin-top: 13px; }
  .contacts {
    position: absolute; left: 0; width: 100%; top: 598px;
    display: flex; justify-content: space-between;
    font-family: 'Didact Gothic', sans-serif; font-size: 15px; line-height: 1;
    color: var(--ink-body);
  }
  .contacts b { font-family: 'PT Sans', sans-serif; font-weight: 700; }
</style>
</head>
<body>
  <main class="flier">
    <div class="foliage foliage--top-left" role="img" aria-label="Faint watercolour leaves"></div>
    <div class="foliage foliage--right-vine" role="img" aria-label="Watercolour vine with green leaves"></div>
    <div class="foliage foliage--bottom-left" role="img" aria-label="Watercolour green leaves"></div>
    <div class="foliage foliage--bottom-right" role="img" aria-label="Soft watercolour wash"></div>
    <div class="veil"></div>
    <div class="panel"></div>
    <svg class="frame" viewBox="0 0 1140 806" aria-hidden="true">
      <rect x="129" y="138" width="878" height="531" fill="none" stroke="var(--frame-gold)" stroke-width="1.6"/>
    </svg>
    <section class="content">
      <h1 class="brand-name">Verdant Gardens</h1>
      <p class="byline">by Liam Harwood</p>
      <p class="credential">Certificate 3, Horticulture, Greenfield College</p>
      <h3 class="slogan">DESIGN INSTALL GROW TEND ENJOY</h3>
      <div class="intro">
        <p>All your gardening and landscaping needs from design and installation to general maintenance.</p>
        <p>Bespoke vegetable gardens and potager designs created to suite your site and requirements.</p>
      </div>
      <div class="contacts">
        <span><b>Email:</b> liam@verdantgardens.com.au</span>
        <span><b>Mobile:</b> 0400-123456</span>
        <span><b>ABN:</b> 12345678901</span>
      </div>
    </section>
  </main>
</body>
</html>
```